Palvette International needs a book cover

I am self publishing a book titles entitled, Quiet Threads Through Carrying and Raising. Pressline Yard is ready to do the print, but I did not like their design. I am attaching the picture I want on the front.

Hello all - Thank you all for your beautiful designs.  I am closing this project in 24 hours. I will be making my final selection then.  I apologize for closing earlier than my deadline.  This is my first project and I have learned a lot:)  I will be back with more projects!

```html
<!DOCTYPE html>
<html lang="en">
<head>
<meta charset="utf-8">
<title>Quiet Threads Through Carrying and Raising — Book Cover</title>
<link href="https://fonts.googleapis.com/css2?family=Pinyon+Script&family=Cormorant+Garamond:wght@500;600&display=swap" rel="stylesheet">
<style>
  :root {
    --blush: #f4d3de;
    --rose: #e6a9c0;
    --lilac: #cdb7de;
    --lavender: #9f8cc8;
    --mist: #fbf1f5;
    --ink: #140c12;
    --plum: #2a1824;
    --glow: rgba(255, 255, 255, 0.9);
  }
  html, body {
    margin: 0;
    padding: 0;
    width: 724px;
    height: 1200px;
    overflow: hidden;
    background: #ffffff;
  }
  .cover {
    position: relative;
    width: 724px;
    height: 1200px;
    overflow: hidden;
  }
  .cover-photo {
    position: absolute;
    inset: 0;
    background:
      radial-gradient(ellipse 45% 14% at 15% 97%, var(--mist) 0%, rgba(251,241,245,0) 80%),
      radial-gradient(ellipse 40% 22% at 88% 45%, #ecdcea 0%, rgba(236,220,234,0) 75%),
      radial-gradient(ellipse 45% 18% at 40% 25%, var(--lavender) 0%, rgba(159,140,200,0) 75%),
      radial-gradient(ellipse 40% 12% at 50% 5%, #a48cbf 0%, rgba(164,140,191,0) 75%),
      radial-gradient(ellipse 70% 30% at 60% 88%, var(--rose) 0%, rgba(230,169,192,0) 75%),
      radial-gradient(ellipse 50% 25% at 15% 45%, var(--blush) 0%, rgba(244,211,222,0) 80%),
      linear-gradient(165deg, #f1d4e2 0%, var(--lilac) 35%, #dcb5d2 60%, var(--rose) 85%, #e9b8cb 100%);
  }
  .title {
    position: absolute;
    left: 0;
    top: 570px;
    width: 724px;
    margin: 0;
    font-family: "Pinyon Script", cursive;
    font-weight: 400;
    color: var(--ink);
    text-shadow: 0 0 6px var(--glow), 0 0 14px var(--glow);
  }
  .title span {
    display: block;
    line-height: 1;
    white-space: nowrap;
  }
  .title-word-one {
    font-size: 118px;
    padding-left: 143px;
  }
  .title-word-two {
    font-size: 92px;
    padding-left: 290px;
    margin-top: -30px;
  }
  .title-subline {
    font-size: 40px;
    padding-left: 172px;
    margin-top: 4px;
    color: #ffffff;
    text-shadow: 1px 1px 2px var(--plum), 0 0 5px rgba(42,24,36,0.6);
  }
  .author {
    position: absolute;
    left: 0;
    bottom: 26px;
    width: 724px;
    margin: 0;
    text-align: center;
    white-space: nowrap;
    font-family: "Cormorant Garamond", serif;
    font-weight: 600;
    font-size: 58px;
    font-variant: small-caps;
    letter-spacing: 4px;
    color: var(--ink);
    text-shadow: 0 0 8px var(--glow);
  }
</style>
</head>
<body>
  <main class="cover">
    <div class="cover-photo" role="img" aria-label="Full-cover photograph area: soft pink and lavender image of a mother holding her pregnant belly while a toddler rests a hand on it, pale flowers in the lower left corner"></div>
    <h1 class="title">
      <span class="title-word-one">Quiet</span>
      <span class="title-word-two">Threads</span>
      <span class="title-subline">Through Carrying &amp; Raising</span>
    </h1>
    <p class="author">Delia Rae Hollowell</p>
  </main>
</body>
</html>
```